Kelto Mobile Apps Needs banners for webpage

We need a top banner. We are a mobile app developer for the Hospitality Industry. We are developing a Loyalty Program with the trade name KeltoPerks. The banner will be used on our loyalty page inside our website.Please see www.keltomobileapps-example.com to understand our theme. The banner should be 1700 X 470.

Please see the attached banner. This is from a competitor website.Please use it as a model and make changes...... make it unique to KeltoMobile. I need to convey the same message as this banner. Same statistics. Same setting (restaurant).

I have added a purchased vector file for the restaurant setting. I noticed many are struggling and using stock art which I don't like.Work with the background color. Make it more playful--pastels--less formal. Be creative!

Do not wait till that last day of the contest to submit. I might take the first design I like and proceed. The sooner you post a design, the better direction I can give you.
Updates

Reason: Not getting any designs I can work with yet. Please give me ideas.

All, Please re-read the brief. I have changed the banner project. It will be much easier but I need it quickly.

Now that I have made this banner much easier, I would like to wrap this contest up. Don't wait till the last day to post designs. The first design I like I will go with and close the project. Be creative, colorful, imaginative! Good luck. Martin Orvane Kelto Mobile Apps, LLC morvane@

All. See the vector file that I just purchased for the background image. Can you try different background colors. I still need the other content showing the percentages of loyalty. I do not want the rocket ship!

All, I have updated the brief. I have included a vector file that has a perfect restaurant scene. Please be creative and work with colors in this scene. Also be creative with the information in the circles showing the metrics of loyalty. Do not use the Rocket. If you find another idea to replace the rocket, that's fine. Or, just leave it off. Please make this banner unique!

Target Market(s)

Hospitality Industry.

Industry/Entity Type

Restaurant

Requirements
Must have
• Banner should be beautiful.. Image of diners at restaurant along with the statistics and message "Boost Sales".
Nice to have
• Our banner should convey the same message as the attached but we must re-design because the attached banner belongs to another company.
Should not have
• Do not re-use any of the images in the attached banner. This is from my competitor. Do not use a rocket for "Boost Sales" image.

```html
<!DOCTYPE html>
<html lang="en">
<head>
<meta charset="utf-8">
<title>Boost Sales Banner</title>
<link href="https://fonts.googleapis.com/css2?family=Arvo:wght@700&family=Roboto+Condensed:wght@400;500&family=Playfair+Display:ital,wght@1,800&display=swap" rel="stylesheet">
<style>
  :root {
    --peach: #ffd9c2;
    --peach-light: #ffe9db;
    --blush: #f7b8c4;
    --lavender: #cdb9ef;
    --mint: #b5e6d3;
    --sky: #bfe0f5;
    --badge: #f08a8f;
    --badge-edge: #ffffff;
    --white: #ffffff;
    --accent: #ee5a5f;
    --ink: #4a3550;
    --scene-tone: rgba(214, 140, 160, 0.45);
  }
  * { margin: 0; padding: 0; box-sizing: border-box; }
  html, body { width: 1200px; height: 331px; overflow: hidden; background: var(--peach); }
  .banner {
    position: relative;
    width: 1200px;
    height: 331px;
    overflow: hidden;
    background: linear-gradient(120deg, var(--peach-light) 0%, var(--peach) 45%, #fcd0d6 100%);
    font-family: "Roboto Condensed", "Arial Narrow", sans-serif;
  }
  .restaurant-scene {
    position: absolute;
    inset: 0;
    background:
      radial-gradient(ellipse 240px 230px at 60px 210px, var(--scene-tone), transparent 70%),
      radial-gradient(ellipse 230px 250px at 1000px 170px, rgba(190, 160, 230, 0.45), transparent 70%),
      radial-gradient(ellipse 160px 220px at 1160px 240px, var(--scene-tone), transparent 70%),
      linear-gradient(180deg, rgba(214, 140, 160, 0) 60%, rgba(214, 140, 160, 0.35) 100%);
  }
  .headline-badge {
    position: absolute;
    left: 392px;
    top: -152px;
    width: 416px;
    height: 252px;
    border-radius: 50%;
    background: var(--badge);
    border: 2px solid var(--badge-edge);
  }
  .headline {
    position: absolute;
    left: 0;
    width: 1200px;
    top: 17px;
    text-align: center;
    color: var(--white);
  }
  .headline-title {
    font-family: "Arvo", Rockwell, serif;
    font-weight: 700;
    font-size: 31px;
    line-height: 38px;
    letter-spacing: 0.5px;
  }
  .headline-sub {
    font-size: 9px;
    line-height: 12px;
    margin-top: 2px;
  }
  .stat {
    position: absolute;
    top: 144px;
    width: 264px;
    height: 138px;
    border-radius: 50%;
    box-shadow: 0 0 8px rgba(255, 255, 255, 0.7);
  }
  .stat-inner {
    position: absolute;
    inset: 11px;
    border-radius: 50%;
    background: var(--white);
    display: flex;
    flex-direction: column;
    align-items: center;
    justify-content: center;
    color: var(--ink);
    text-align: center;
  }
  .stat-visits { left: 148px; background: var(--mint); }
  .stat-spend { left: 468px; background: var(--lavender); }
  .stat-value { left: 780px; background: var(--sky); }
  .stat-label { font-size: 14.5px; font-weight: 500; line-height: 18px; }
  .stat-number {
    font-family: "Playfair Display", Georgia, serif;
    font-style: italic;
    font-weight: 800;
    font-size: 38px;
    line-height: 44px;
    color: var(--accent);
    margin: 3px 0 2px;
  }
  .guest-icons { display: block; margin: 6px 0 5px; }
</style>
</head>
<body>
  <div class="banner">
    <div class="restaurant-scene" role="img" aria-label="Soft pastel restaurant scene with a waiter serving diners at tables"></div>

    <div class="headline-badge"></div>
    <div class="headline">
      <div class="headline-title">Boost Sales</div>
      <div class="headline-sub">Loyal Guest vs. Average Guest</div>
    </div>

    <div class="stat stat-visits">
      <div class="stat-inner">
        <div class="stat-label">Loyal Guests Visit About</div>
        <div class="stat-number">32%</div>
        <div class="stat-label">More Than Average Guests</div>
      </div>
    </div>

    <div class="stat stat-spend">
      <div class="stat-inner">
        <div class="stat-label">Loyal Guests Spend About</div>
        <div class="stat-number">25%</div>
        <div class="stat-label">More Than Average Guests</div>
      </div>
    </div>

    <div class="stat stat-value">
      <div class="stat-inner">
        <div class="stat-label">1 Loyal Guest =</div>
        <svg class="guest-icons" width="114" height="40" viewBox="0 0 114 40" aria-hidden="true">
          <g fill="#ee5a5f">
            <circle cx="18" cy="10" r="8"/>
            <path d="M2 40 C2 26 8 21 18 21 C28 21 34 26 34 40 Z"/>
            <path d="M15 21 L21 21 L19.5 25 L21 34 L18 37 L15 34 L16.5 25 Z" fill="#ffffff"/>
            <path d="M44 18 L50 22 L44 26 L46 22 Z M52 18 L58 22 L52 26 L54 22 Z"/>
            <circle cx="72" cy="13" r="5.5"/>
            <path d="M62 34 C62 24 66 21 72 21 C78 21 82 24 82 34 Z"/>
            <circle cx="102" cy="13" r="5.5"/>
            <path d="M92 34 C92 24 96 21 102 21 C108 21 112 24 112 34 Z"/>
            <circle cx="87" cy="11" r="6.5" stroke="#ffffff" stroke-width="1.5"/>
            <path d="M75 36 C75 24 80 20 87 20 C94 20 99 24 99 36 Z" stroke="#ffffff" stroke-width="1.5"/>
          </g>
        </svg>
        <div class="stat-label">Average Guest 10</div>
      </div>
    </div>
  </div>
</body>
</html>
```